Lose Up To 1 LB Of Fat Per Day

We need a double sided street sign for our weight loss clinic. We need the doctors picture to the right side of the sign and we need a challenge “Lose Up To 1 Pound Of Fat Per Day” included in the signage.
Our color scheme for the clinic are black, white, teal and silver.
The phone number should be at the bottom of the sign
555-206–3948

Target Market(s)

Weight Loss

Font styles to use
Sans Serif

```html
<!DOCTYPE html>
<html lang="en">
<head>
<meta charset="utf-8">
<title>Weight Loss Clinic Street Sign</title>
<link rel="stylesheet" href="https://fonts.googleapis.com/css2?family=Montserrat:wght@700;800&display=swap">
<style>
  :root {
    --page: #e2e2e2;
    --teal: #0c8b8a;
    --teal-light: #219a98;
    --teal-dark: #0a6868;
    --white: #ffffff;
    --band: #f4f4f4;
    --silver-light: #ececec;
    --silver-dark: #9c9c9c;
  }
  html, body {
    margin: 0;
    padding: 0;
    width: 1200px;
    height: 864px;
    overflow: hidden;
    background: var(--page);
  }
  .sign {
    position: absolute;
    left: 20px;
    top: 142px;
    width: 1160px;
    height: 579px;
    overflow: hidden;
    font-family: "Montserrat", sans-serif;
    font-weight: 700;
  }
  .sign-art {
    position: absolute;
    inset: 0;
    width: 1160px;
    height: 579px;
  }
  .headline {
    position: absolute;
    left: 14px;
    width: 606px;
    margin: 0;
    text-align: center;
    line-height: 1;
    white-space: nowrap;
  }
  .headline-lose {
    top: 86px;
    font-size: 84px;
    font-weight: 800;
    color: var(--white);
    letter-spacing: 1px;
  }
  .headline-pound {
    top: 215px;
    font-size: 54px;
    color: var(--teal);
  }
  .headline-day {
    top: 307px;
    font-size: 68px;
    color: var(--white);
  }
  .phone-box {
    position: absolute;
    left: 38px;
    top: 448px;
    width: 576px;
    height: 131px;
    background: var(--band);
    border-radius: 36px 36px 0 0;
    display: flex;
    align-items: center;
    justify-content: center;
  }
  .phone-number {
    margin: 0 0 8px;
    font-size: 64px;
    font-weight: 800;
    color: var(--teal-dark);
    letter-spacing: 0.5px;
    white-space: nowrap;
  }
</style>
</head>
<body>
  <main class="sign">
    <svg class="sign-art" viewBox="0 0 1160 579" xmlns="http://www.w3.org/2000/svg">
      <defs>
        <linearGradient id="tealField" x1="0" y1="0" x2="1" y2="1">
          <stop offset="0" stop-color="#219a98"/>
          <stop offset="0.55" stop-color="#0c8b8a"/>
          <stop offset="1" stop-color="#0c8b8a"/>
        </linearGradient>
        <radialGradient id="portraitBackdrop" gradientUnits="userSpaceOnUse" cx="830" cy="330" r="360">
          <stop offset="0" stop-color="#ececec"/>
          <stop offset="1" stop-color="#9c9c9c"/>
        </radialGradient>
      </defs>
      <rect class="teal-field" x="0" y="0" width="1160" height="579" fill="url(#tealField)"/>
      <rect class="headline-band" x="0" y="194" width="1160" height="97" fill="#f4f4f4"/>
      <g class="doctor-portrait" role="img" aria-label="Photo of the clinic doctor in a dark suit and purple tie, standing against a silver backdrop">
        <rect x="940" y="0" width="220" height="579" fill="url(#portraitBackdrop)"/>
        <circle cx="940" cy="306" r="312" fill="url(#portraitBackdrop)"/>
      </g>
    </svg>

    <h1 class="headline headline-lose">LOSE UP TO</h1>
    <p class="headline headline-pound">A POUND OF FAT</p>
    <p class="headline headline-day">PER DAY</p>

    <div class="phone-box">
      <p class="phone-number"># 555 206 3948</p>
    </div>
  </main>
</body>
</html>
```